Design Short Report for Non Governmental Organisation

We need a graphic designer to help us turn a basic Word report (1 graph, 10 pages of text) into an engaging public document. The content is pretty straightforward and we can provide all the imagery necessary.

Few design restrictions apply:

Font: Trebuchet
Colors: black, white and green (Pantone 38, R (105), G (190), B (40)

Attached you will find the full copy of the report that needs to be designed.

If you want to see what our other public documents look like, and the general style we use, you can find examples here:

www.fieldreliefnetwork.org.uk/publications

Industry/Entity Type

Graphic Designer

Font styles to use
Other font styles liked:
• Trebuchet

Colors
acd037

Requirements
Must have
• Short report, modern feel.
• Font: Trebuchet
• Colors: black, white and green (Pantone 38, R (105), G (190), B (40)
Nice to have
• Picture spreads. Full picture on cover (no frames or edges), and a couple of pictures on the inside would help. All photographic material can be found here.
• https://dl.boxcrateusercontent.com/u/73916258/Pictures%20for%20KEL2020.zip

```html
<!DOCTYPE html>
<html lang="en">
<head>
<meta charset="utf-8">
<title>Inner Page – Short Report</title>
<link href="https://fonts.googleapis.com/css2?family=Open+Sans:wght@400;600;700&family=Roboto+Condensed:wght@700&display=swap" rel="stylesheet">
<style>
  :root {
    --brand-green: #69be28;
    --brand-green-dark: #3f7f14;
    --brand-green-light: #9bd65f;
    --ink: #1a1a1a;
    --text-grey: #3c3c3c;
    --rule-grey: #c9c9c9;
    --tab-grey: #e4e4e4;
    --paper: #ffffff;
  }
  * { box-sizing: border-box; margin: 0; padding: 0; }
  html, body { width: 853px; height: 1200px; overflow: hidden; background: var(--paper); }
  body { font-family: "Open Sans", "Trebuchet MS", sans-serif; color: var(--text-grey); position: relative; }

  .page-header {
    position: absolute; top: 0; left: 0; width: 853px; height: 58px;
    background: linear-gradient(90deg, var(--brand-green-dark) 0%, var(--brand-green) 60%, var(--brand-green-light) 100%);
    border-bottom: 5px solid var(--ink);
  }
  .page-title {
    position: absolute; left: 22px; top: 10px;
    font-family: "Roboto Condensed", "Trebuchet MS", sans-serif;
    color: #fff; font-weight: 700; font-size: 30px; letter-spacing: 0.2px;
  }

  .content { position: absolute; top: 112px; left: 34px; width: 786px; }

  .section-heading {
    margin-left: 14px;
    color: var(--brand-green-dark); font-weight: 700; font-size: 24px;
    padding-bottom: 8px; border-bottom: 2px solid var(--rule-grey);
  }
  .section-subtitle {
    margin: 18px 0 2px 14px;
    color: var(--brand-green-dark); font-weight: 700; font-size: 20px;
  }
  .body-copy {
    font-size: 16.6px; line-height: 31.5px; text-align: justify; margin-bottom: 24px;
  }
  .body-copy.lead { margin-left: 14px; margin-bottom: 16px; }

  .page-footer {
    position: absolute; left: 0; bottom: 0; width: 853px; height: 64px;
  }
  .footer-rule { position: absolute; left: 0; right: 0; top: 18px; height: 2px; background: var(--rule-grey); }
  .page-number {
    position: absolute; left: 0; top: 20px; width: 60px; height: 44px;
    background: var(--tab-grey); color: var(--text-grey);
    font-size: 18px; font-weight: 600; padding: 10px 0 0 24px;
    border-left: 6px solid var(--brand-green);
  }
  .org-mark {
    position: absolute; right: 22px; top: 22px;
    display: flex; align-items: center; gap: 6px;
  }
  .org-mark .dot { width: 12px; height: 12px; border-radius: 50%; background: var(--brand-green); }
  .org-mark .name { color: var(--ink); font-weight: 700; font-size: 28px; }
</style>
</head>
<body>
  <header class="page-header">
    <h1 class="page-title">INNER PAGES TITLE HERE</h1>
  </header>

  <main class="content">
    <h2 class="section-heading">Heading Title Here</h2>
    <h3 class="section-subtitle">Subtitle Here</h3>
    <p class="body-copy lead">Lorem Ipsum is simply dummy text of the printing and typesetting industry. Lorem Ipsum has been the industry's industry. Lorem Ipsum has been the finishLorem Ipsum is simply dummy text of the printing and typesetting industry. Lorem Ipsum has been the industry's industry. Lorem Ipsum has been the finishLorem Ipsum is simply dummy text of the printing and typesetting industry. Lorem Ipsum has been the industry's industry. Lorem Ipsum has been the finishLorem Ipsum is simply dummy text of the printing and typesetting industry. Lorem Ipsum has been the industry's industry. Lorem Ipsum has been the finish.</p>

    <p class="body-copy">Lorem Ipsum is simply dummy text of the printing and typesetting industry. Lorem Ipsum has been the industry's industry. Lorem Ipsum has been the finishLorem Ipsum is simply dummy text of the printing and typesetting industry. Lorem Ipsum has been the industry's industry. Lorem Ipsum has been the finish</p>

    <p class="body-copy">Lorem Ipsum is simply dummy text of the printing and typesetting industry. Lorem Ipsum has been the industry's industry. Lorem Ipsum has been the finishLorem Ipsum is simply dummy text of the printing and typesetting industry.</p>

    <p class="body-copy">Lorem Ipsum has been the industry's industry. Lorem Ipsum has been the finish.</p>

    <p class="body-copy">Lorem Ipsum is simply dummy text of the printing and typesetting industry. Lorem Ipsum has been the industry's industry. Lorem Ipsum has been the finishLorem Ipsum is simply dummy text of the printing and typesetting industry. Lorem Ipsum has been the industry's industry. Lorem Ipsum has been the finish</p>

    <p class="body-copy">Lorem Ipsum is simply dummy text of the printing and typesetting industry. Lorem Ipsum has been the industry's industry. Lorem Ipsum has been the finishLorem Ipsum is simply dummy text of the printing and typesetting industry.</p>
  </main>

  <footer class="page-footer">
    <div class="footer-rule"></div>
    <div class="page-number">01</div>
    <div class="org-mark">
      <span class="dot"></span>
      <span class="name">FRN</span>
    </div>
  </footer>
</body>
</html>
```